vantrel works cybersecurity website design and development

website design and development for a cybersecurity company. we have a logo and would like site to suit logo colors and look
cybersecurity website should be secure and look professional
main example of site we want to use: https://www.morvisquad.example/
site should be usable on tablet and phones

For each design proposal, please could you provide details of what language you'll use to code the website.

Target Market(s)

insurance companies, financial institutions, private SME, Africa and Europe

Coding

Coded - Design and coding required

Number of Pages Required

5+ page

Requirements
Must have
• 9 Pages:
Home
About us
Contacts
Partners
Blog
Services
( consulting, vulnerability assessment, information systems security audit, ISO compliance, Penetration testing, security awareness training, social engineering test, protection against DDoS, procurement )
Resources
Technologies
Careers
Nice to have
• nice to have all services have their own pages.
design based on logo colors and look

please provide what will be use to code the website

```html
<!DOCTYPE html>
<html lang="en">
<head>
<meta charset="utf-8">
<title>Vantrel Works – Cyber Security</title>
<link href="https://fonts.googleapis.com/css2?family=Poppins:wght@400;500;600;700&display=swap" rel="stylesheet">
<style>
:root{
  --navy:#041226;
  --navy-2:#0a2547;
  --blue:#0d5fae;
  --blue-bright:#1a86dc;
  --cyan:#37c4f2;
  --ink:#1b1f2a;
  --muted:#6b7280;
  --card:#f3f4f6;
  --stage:#eef0f3;
  --white:#ffffff;
}
*{box-sizing:border-box;margin:0;padding:0}
html,body{width:1200px;height:3124px;overflow:hidden}
body{background:var(--stage);font-family:"Poppins",sans-serif;color:var(--ink);position:relative}
.page{position:absolute;left:192px;top:72px;width:816px;height:2992px;background:var(--white);overflow:hidden;box-shadow:0 6px 30px rgba(0,0,0,.18)}
.abs{position:absolute}
.hero{left:0;top:0;width:816px;height:488px;background:radial-gradient(circle at 75% 40%,#0b3563 0%,var(--navy) 55%)}
.brand{left:40px;top:28px;display:flex;align-items:center;gap:8px;color:var(--white);font-weight:600;font-size:17px}
.brand i{width:22px;height:22px;border-radius:50%;background:var(--blue-bright);display:block}
.nav{right:40px;top:36px;display:flex;gap:18px;font-size:9px;color:#cfd8e6}
.hero-title{left:48px;top:206px;font-size:38px;font-weight:700;color:var(--white)}
.hero-title span{color:var(--blue-bright)}
.hero-text{left:48px;top:258px;width:250px;font-size:8px;line-height:1.5;color:#b7c3d4}
.btn{display:inline-block;background:var(--blue);color:var(--white);font-size:9px;font-weight:500;padding:8px 16px}
.hero-art{left:448px;top:60px;width:330px;height:360px;border-radius:50%;background:radial-gradient(circle,#1fa8e8 0%,#0b4d8f 45%,rgba(4,18,38,0) 72%)}
.feature{top:476px;width:204px;height:92px;background:var(--white);box-shadow:0 4px 14px rgba(0,0,0,.15);padding:14px 16px}
.feature h4{font-size:10px;font-weight:600;color:var(--blue);display:flex;align-items:center;gap:6px}
.feature p{font-size:7px;line-height:1.5;color:var(--muted);margin-top:6px}
.about-art{left:68px;top:608px;width:260px;height:300px;background:linear-gradient(160deg,#0b2f5a,#1a86dc);clip-path:polygon(0 0,100% 0,100% 55%,50% 100%,0 55%)}
.h2{font-size:20px;font-weight:700;color:var(--ink)}
.h2 span{color:var(--blue-bright)}
.about-text{left:376px;top:680px;width:376px;font-size:8.5px;line-height:1.6;color:#444}
.center{left:0;width:816px;text-align:center}
.service{top:1056px;width:196px;height:164px;background:var(--card);text-align:center;padding-top:36px;font-size:11px;font-weight:500;color:var(--ink)}
.service.active{top:1040px;height:196px;width:220px;background:linear-gradient(160deg,var(--blue),#0a3f7a);color:var(--white);padding-top:48px}
.service svg{display:block;margin:0 auto 14px}
.tech{left:0;top:1300px;width:816px;height:420px;background:linear-gradient(120deg,var(--blue-bright),var(--blue) 50%,#083c78);clip-path:polygon(0 40px,100% 0,100% 380px,0 420px)}
.tech-art{left:68px;top:1380px;width:330px;height:280px;background:linear-gradient(150deg,#e6f1fb,#6fb4ea);border-radius:8px;opacity:.9}
.tech-title{left:460px;top:1390px;color:var(--white);font-size:18px;font-weight:700}
.tech-list{left:460px;top:1440px;list-style:none;color:#e6f0fb;font-size:9px}
.tech-list li{display:flex;align-items:center;gap:8px;margin-bottom:12px}
.blog-img{top:1768px;width:216px;height:200px;background:linear-gradient(160deg,#0a2547,#1a6fb8)}
.blog-text{top:1982px;width:216px;font-size:8px;color:#555;line-height:1.5}
.blog-text h5{font-size:11px;font-weight:600;color:var(--ink);margin-bottom:4px}
.blog-text a{color:var(--blue);font-weight:500;text-decoration:none;display:block;margin-top:4px}
.partner{top:2212px;width:160px;height:56px;background:var(--card);display:flex;align-items:center;justify-content:center;font-size:17px;font-weight:600;color:var(--ink)}
.footer{left:0;top:2480px;width:816px;height:512px;background:var(--navy);clip-path:polygon(0 80px,100% 0,100% 100%,0 100%)}
.contact{left:68px;top:2316px;width:680px;height:330px;background:linear-gradient(160deg,var(--blue-bright),var(--blue) 60%,#0a3f7a);padding:30px 40px;color:var(--white);text-align:center}
.contact h3{font-size:14px;font-weight:600;line-height:1.5}
.fields{display:flex;gap:10px;margin-top:26px}
.field{flex:1;height:26px;border:1px solid rgba(255,255,255,.6);font-size:8px;text-align:left;padding:7px 8px;color:#dbe8f6}
.message{height:96px;margin-top:10px}
.contact .send{margin-top:16px;background:transparent;border:1px solid var(--white)}
.f-brand{left:0;width:816px;top:2700px;display:flex;justify-content:center;align-items:center;gap:8px;color:var(--white);font-size:20px;font-weight:600}
.f-brand i{width:26px;height:26px;border-radius:50%;background:var(--blue-bright);display:block}
.f-nav{top:2768px;left:0;width:816px;display:flex;justify-content:center;gap:18px;font-size:8.5px;color:#c7d2e2}
.f-col{top:2820px;color:#c7d2e2;font-size:8px;line-height:2}
.f-col h6{color:var(--white);font-size:10px;font-weight:600;margin-bottom:6px}
.sub{height:22px;width:150px;background:var(--white);margin-top:4px}
.sub-btn{background:var(--blue);color:var(--white);font-size:8px;padding:4px 10px;display:inline-block;margin-top:6px}
</style>
</head>
<body>
<main class="page">
  <section class="abs hero"></section>
  <div class="abs brand"><i></i>vantrel works</div>
  <nav class="abs nav"><span>Home</span><span>About us</span><span>Contacts</span><span>Partners</span><span>Blog</span><span>Services</span><span>Technologies</span><span>Careers</span></nav>
  <h1 class="abs hero-title">Cyber <span>Security</span></h1>
  <p class="abs hero-text">We protect the systems and data of insurers, banks and growing businesses across Africa and Europe, with clear advice and steady defence every day.</p>
  <a class="abs btn" style="left:48px;top:316px">Contact Us</a>
  <div class="abs hero-art" role="img" aria-label="Glowing digital shield with keyhole illustration"></div>

  <div class="abs feature" style="left:68px"><h4><svg width="10" height="12" viewBox="0 0 10 12"><path d="M5 0L10 2v4c0 3-2 5-5 6C2 11 0 9 0 6V2z" fill="#1a86dc"/></svg>Security</h4><p>We watch your networks closely and stop threats early, before any harm reaches your clients.</p></div>
  <div class="abs feature" style="left:298px"><h4><svg width="10" height="12" viewBox="0 0 10 12"><rect x="1" y="5" width="8" height="7" fill="#1a86dc"/><path d="M2.5 5V3.5a2.5 2.5 0 015 0V5" stroke="#1a86dc" fill="none"/></svg>Privacy</h4><p>Your private records stay private, guarded by strong controls and careful handling at all times.</p></div>
  <div class="abs feature" style="left:528px"><h4><svg width="12" height="12" viewBox="0 0 12 12"><circle cx="6" cy="5" r="4" fill="#1a86dc"/><path d="M3 8l-1 4 4-2 4 2-1-4" fill="#1a86dc"/></svg>Industry Certified</h4><p>Our team holds recognised credentials and follows proven standards across every engagement.</p></div>

  <div class="abs about-art" role="img" aria-label="Person wearing a VR headset with security icons, in a shield frame"></div>
  <h2 class="abs h2" style="left:376px;top:636px">About <span>Us</span></h2>
  <p class="abs about-text">It is a long established fact that a reader will be distracted by the readable content of a page when looking at its layout. The point of using steady text is that it has a more-or-less normal distribution of letters, as opposed to using placeholder words, making it look like readable English. Many publishing packages and web page editors now use plain text as their default model text, and a search will uncover many web sites still in their infancy.</p>
  <a class="abs btn" style="left:376px;top:850px">Contact Us</a>

  <h2 class="abs h2 center" style="top:1000px">Our <span>Service</span></h2>
  <div class="abs service" style="left:80px"><svg width="30" height="34" viewBox="0 0 30 34"><path d="M15 0l15 5v11c0 9-7 15-15 18C7 31 0 25 0 16V5z" fill="#0d5fae"/><rect x="10" y="15" width="10" height="8" fill="#fff"/></svg>Security<br>Assessment</div>
  <div class="abs service active" style="left:298px"><svg width="34" height="30" viewBox="0 0 34 30"><rect x="1" y="1" width="32" height="22" fill="none" stroke="#fff" stroke-width="2"/><rect x="12" y="8" width="10" height="9" fill="#fff"/><path d="M10 29h14" stroke="#fff" stroke-width="2"/></svg>Security<br>Enhancement</div>
  <div class="abs service" style="left:540px"><svg width="34" height="32" viewBox="0 0 34 32"><path d="M17 0l17 8H0z" fill="#0d5fae"/><rect x="4" y="11" width="4" height="15" fill="#0d5fae"/><rect x="15" y="11" width="4" height="15" fill="#0d5fae"/><rect x="26" y="11" width="4" height="15" fill="#0d5fae"/><rect x="0" y="28" width="34" height="4" fill="#0d5fae"/></svg>Governance ,Risk<br>and Compliance</div>
  <a class="abs btn" style="left:376px;top:1258px;background:var(--navy-2)">View All</a>

  <section class="abs tech"></section>
  <div class="abs tech-art" role="img" aria-label="Isometric illustration of a laptop with a padlock and data screens"></div>
  <h2 class="abs tech-title">Our Technologies</h2>
  <ul class="abs tech-list">
    <li><svg width="12" height="12"><circle cx="6" cy="6" r="5" fill="none" stroke="#fff"/></svg>Cyber Security Artificial Intelligence &amp; Deep learning</li>
    <li><svg width="12" height="12"><circle cx="6" cy="6" r="5" fill="none" stroke="#fff"/></svg>Behavioral Analytics</li>
    <li><svg width="12" height="12"><circle cx="6" cy="6" r="5" fill="none" stroke="#fff"/></svg>Embedded Hardware Authentication</li>
    <li><svg width="12" height="12"><circle cx="6" cy="6" r="5" fill="none" stroke="#fff"/></svg>Blockchain Cybersecurity</li>
    <li><svg width="12" height="12"><circle cx="6" cy="6" r="5" fill="none" stroke="#fff"/></svg>Zero-Trust Model</li>
  </ul>
  <a class="abs btn" style="left:460px;top:1606px;background:var(--blue-bright)">Contact Us</a>

  <h2 class="abs h2 center" style="top:1716px">Our <span>Blogs</span></h2>
  <div class="abs blog-img" style="left:64px" role="img" aria-label="Hands typing on a keyboard in a dark room"></div>
  <div class="abs blog-img" style="left:300px" role="img" aria-label="Digital shield on a blue circuit background"></div>
  <div class="abs blog-img" style="left:536px;background:linear-gradient(160deg,#3a3f48,#8a8f99)" role="img" aria-label="Close-up of a circuit board with a chip"></div>
  <div class="abs blog-text" style="left:64px"><h5>It is a long established fact</h5>Many publishing packages and web page editors now use it.<a>Read More</a></div>
  <div class="abs blog-text" style="left:300px"><h5>It is a long established fact</h5>Many publishing packages and web page editors now use it.<a>Read More</a></div>
  <div class="abs blog-text" style="left:536px"><h5>It is a long established fact</h5>Many publishing packages and web page editors now use it.<a>Read More</a></div>

  <h2 class="abs h2 center" style="top:2150px">They already <span>trusted us</span></h2>
  <div class="abs partner" style="left:64px">Logo</div>
  <div class="abs partner" style="left:248px">Ardent</div>
  <div class="abs partner" style="left:432px;background:var(--white);box-shadow:0 3px 10px rgba(0,0,0,.12)">Tessara</div>
  <div class="abs partner" style="left:616px">Quillby</div>

  <section class="abs footer"></section>
  <section class="abs contact">
    <h3>Contact Us Today To Speak With<br>An Expert About Your Specific Needs</h3>
    <div class="fields"><div class="field">Name</div><div class="field">Phone number</div><div class="field">Email</div></div>
    <div class="field message">Message</div>
    <a class="btn send">Send Message</a>
  </section>

  <div class="abs f-brand"><i></i>vantrel works</div>
  <nav class="abs f-nav"><span>Home</span><span>About us</span><span>Contacts</span><span>Partners</span><span>Blog</span><span>Services</span><span>Technologies</span><span>Careers</span></nav>
  <div class="abs f-col" style="left:68px"><h6>Contact Us</h6>
    <div>12 Harbour Lane, Unit 4</div><div>hello@vantrelworks.example</div><div>+00 120 4455</div></div>
  <div class="abs f-col" style="left:248px"><h6>Resources</h6><div>Blog</div><div>Partners</div><div>Careers</div><div>Privacy policy</div></div>
  <div class="abs f-col" style="left:410px"><h6>Follow Us</h6><div>Network</div><div>Updates</div><div>Videos</div><div>News</div></div>
  <div class="abs f-col" style="left:580px"><h6>Subscribe newsletter</h6><div class="sub"></div><span class="sub-btn">Subscribe</span></div>
</main>
</body>
</html>
```